Healthcare IT company looking for business card design

We develop IT systems for healthcare that significantly reduces cost and improves quality.

We want a business card design that is professional and clean, and using the colors in our logo.

Target Market(s)

Doctors and decision makers in the healthcare industry

Industry/Entity Type

Healthcare

Contact Information for Business Card

It should include
Name and title, address, telephone

Tobias Vrenholt, CEO
+46 712 418257
tobias@kelvaro.se

Font styles to use
Serif

Colors
0355a3
ed282f

Requirements
Must have
• Clean design
• Professional feel
Nice to have
• N/A
Should not have
• N/A

```html
<!DOCTYPE html>
<html lang="en">
<head>
<meta charset="utf-8">
<title>Kelvaro business cards</title>
<link rel="stylesheet" href="https://fonts.googleapis.com/css2?family=Roboto+Slab:wght@700&display=swap">
<style>
  :root {
    --brand-blue: #0a52ff;
    --brand-red: #ff0a1e;
    --card-white: #ffffff;
    --stage-dark: #000000;
    --stage-glow: #1e1e1e;
  }
  * { margin: 0; padding: 0; box-sizing: border-box; }
  html, body { width: 1200px; height: 1200px; overflow: hidden; }
  body {
    background: radial-gradient(circle at 18% 40%, var(--stage-glow) 0%, var(--stage-dark) 70%);
    font-family: "Roboto Slab", Georgia, serif;
    font-weight: 700;
    position: relative;
  }
  .card {
    position: absolute;
    left: 222px;
    width: 756px;
    height: 472px;
    background: var(--card-white);
    overflow: hidden;
  }
  .card--front { top: 114px; }
  .card--back { top: 614px; }
  .card > * { position: absolute; }

  .bar-blue { background: var(--brand-blue); top: 0; }
  .bar-red { background: var(--brand-red); top: 0; }

  .wordmark {
    left: 66px;
    font-size: 68px;
    line-height: 1;
    color: var(--brand-blue);
    letter-spacing: -1px;
    display: flex;
    align-items: center;
    gap: 12px;
  }
  .wordmark__dot {
    width: 16px; height: 16px;
    border-radius: 50%;
    background: var(--brand-red);
    margin-top: -40px;
  }

  .rule { width: 2px; }
  .rule--red { background: var(--brand-red); }
  .rule--blue { background: var(--brand-blue); }

  .contact {
    text-align: right;
    font-size: 24px;
    line-height: 32px;
    white-space: nowrap;
  }
  .contact .blue { color: var(--brand-blue); }
  .contact .red { color: var(--brand-red); }

  .bands { left: 0; bottom: 0; }
  .corner-block { background: var(--brand-red); border-top-left-radius: 14px; right: 0; bottom: 0; }
</style>
</head>
<body>

<section class="card card--front">
  <div class="bar-blue" style="left:717px;width:19px;height:128px;"></div>
  <div class="bar-red" style="left:736px;width:20px;height:153px;"></div>

  <div class="wordmark" style="top:178px;">Kelvaro<span class="wordmark__dot"></span></div>

  <div class="rule rule--red" style="left:374px;top:144px;height:184px;"></div>
  <div class="rule rule--blue" style="left:380px;top:144px;height:184px;"></div>

  <div class="contact" style="right:68px;top:172px;">
    <p class="blue">TOBIAS VRENHOLT</p>
    <p class="red">CEO</p>
    <p class="blue">+46 712 418257</p>
    <p class="red">tobias@kelvaro.se</p>
  </div>

  <svg class="bands" width="440" height="33" viewBox="0 0 440 33">
    <polygon points="0,0 418,0 428,33 0,33" fill="var(--brand-red)"/>
    <polygon points="0,17 406,17 410,33 0,33" fill="var(--brand-blue)"/>
  </svg>

  <div class="corner-block" style="width:136px;height:142px;"></div>
</section>

<section class="card card--back">
  <div class="bar-blue" style="left:674px;width:31px;height:129px;"></div>
  <div class="bar-red" style="left:705px;width:51px;height:153px;"></div>

  <div class="wordmark" style="top:70px;">Kelvaro<span class="wordmark__dot"></span></div>

  <div class="contact" style="right:410px;top:172px;">
    <p class="blue">TOBIAS VRENHOLT</p>
    <p class="red">CEO</p>
    <p class="blue">+46 712 418257</p>
    <p class="red">tobias@kelvaro.se</p>
  </div>

  <div class="rule rule--red" style="left:360px;top:178px;height:112px;"></div>
  <div class="rule rule--blue" style="left:366px;top:178px;height:112px;"></div>

  <svg class="bands" width="460" height="106" viewBox="0 0 460 106">
    <polygon points="0,0 418,0 453,106 0,106" fill="var(--brand-red)"/>
    <polygon points="0,34 386,34 410,106 0,106" fill="var(--brand-blue)"/>
  </svg>

  <div class="corner-block" style="width:231px;height:230px;"></div>
</section>

</body>
</html>
```